R.Morton LLC Organizational Change and Development

I am starting my own company as a a senior facilitator, keynote speaker, executive coach, webinar training instructor, quality management adviser, and classroom presenter. I have taught diversity and cultural competence, organizational development, change management, leadership, organizational dynamics, team-building, accountability, negotiation, work-life balance, quality management, DISC, and hundreds of web based trainings. I have a PhD. in Counseling Psychology, MBA, B.S. in Human Development, Family Studies, and a Master’s Practitioner of Neurolinguistic Programming. My degrees and certifications give me a foundation for advising a wide variety of people, industries, and cultures at all organizational levels. I would like a design that's fun, engaging, humorous, progressive, and has a professional feel. I really like the colors burgundy wine.

Target Market(s)

corporate America

Industry/Entity Type

Training

Number of Pages Required

5+ page

Colors
eb1f26
f04a50
3176b4
33a6d7

Requirements
Must have
• my different areas of expertise - fun visuals -easy for me to use
Should not have
• something that looks stiff, too traditional or boring

```html
<!DOCTYPE html>
<html lang="en">
<head>
<meta charset="utf-8">
<title>R.Morton — Organizational Change and Development</title>
<link rel="stylesheet" href="https://fonts.googleapis.com/css2?family=Gelasio:wght@400;700&family=Roboto:wght@400;500&display=swap">
<style>
:root{
  --paper:#fbfbf2;
  --wine:#8f2431;
  --wine-dark:#771b27;
  --wine-light:#a1303d;
  --ink:#2f2f2f;
  --bar:#333333;
  --text:#4a4a4a;
  --blue:#1f63a0;
  --photo-a:#8a8a8a;
  --photo-b:#3e3e3e;
}
*{box-sizing:border-box;margin:0;padding:0}
html,body{width:676px;height:1200px;overflow:hidden;background:var(--paper)}
.page{position:relative;width:676px;height:1200px;overflow:hidden;background:var(--paper);font-family:"Roboto",Arial,sans-serif;color:var(--text)}

/* header */
.site-header{position:absolute;left:0;top:0;width:676px;height:49px}
.brand{position:absolute;left:107px;top:9px}
.brand-name{font-family:"Gelasio",Georgia,serif;font-size:23px;color:var(--wine);letter-spacing:.5px;line-height:24px}
.brand-tagline{font-family:"Gelasio",Georgia,serif;font-size:3.4px;letter-spacing:.4px;color:#888;margin-left:20px}
.main-nav{position:absolute;top:18px;left:299px;display:flex;align-items:center}
.main-nav a{font-family:"Gelasio",Georgia,serif;font-size:6.6px;color:var(--ink);text-decoration:none;height:16px;line-height:16px;margin-right:18px}
.main-nav a.active{background:#3a3a3a;color:#fff;padding:0 10px;margin-right:9px}

/* hero */
.hero{position:absolute;left:0;top:49px;width:676px;height:236px;background:linear-gradient(90deg,var(--wine-dark),var(--wine-light) 50%,var(--wine-dark))}
.hero-photo{position:absolute;left:137px;top:16px;width:125px;height:220px;border-radius:60px 60px 0 0;background:linear-gradient(180deg,#d9bf8f 0%,#b69a73 28%,#2a2a2a 45%,#1c1c1c 100%)}
.hero-lead{position:absolute;left:320px;top:65px;font-family:"Gelasio",Georgia,serif;font-size:6.8px;color:#fff}
.hero-title{position:absolute;left:319px;top:76px;font-family:"Gelasio",Georgia,serif;color:#fff;font-weight:400}
.hero-title .big{display:block;font-size:47px;line-height:46px;letter-spacing:.5px}
.hero-title .sub{display:block;font-size:18.5px;line-height:18px;letter-spacing:.3px}
.hero-button{position:absolute;left:320px;top:149px;width:73px;height:22px;background:var(--blue);color:#fff;font-family:"Gelasio",Georgia,serif;font-size:8.5px;line-height:22px;text-align:center}
.hero-arrow{position:absolute;top:111px;width:14px;height:14px}
.hero-arrow.prev{left:106px}
.hero-arrow.next{left:555px}

/* roles bar */
.roles{position:absolute;left:0;top:285px;width:676px;height:75px;background:var(--bar)}
.role{position:absolute;top:0;height:75px;text-align:center;color:#fff;font-family:"Gelasio",Georgia,serif;font-size:6.4px;font-weight:700;line-height:7.6px}
.role svg{display:block;margin:12px auto 6px;width:28px;height:28px}
.role.active{background:var(--wine)}

/* expertise grid */
.area{position:absolute;width:111px;border-bottom:1.2px solid #2e2e2e}
.area-photo{position:relative;width:111px;background:linear-gradient(135deg,var(--photo-a),var(--photo-b))}
.area-photo.short{height:80px}
.area-photo.tall{height:111px}
.plus{position:absolute;right:0;bottom:0;width:13px;height:13px;background:var(--wine);color:#fff;font-size:11px;line-height:13px;text-align:center;font-family:"Roboto",Arial,sans-serif}
.area-title{font-family:"Gelasio",Georgia,serif;font-size:9.6px;line-height:11px;color:var(--wine);font-weight:400;margin:7px 0 7px}
.area-text{font-size:6.2px;line-height:8.7px;color:var(--text)}

/* profile */
.profile{position:absolute;left:0;top:1020px;width:676px;text-align:center}
.avatar{width:72px;height:72px;margin:0 auto;border-radius:50%;border:2px solid var(--wine);background:radial-gradient(circle at 50% 40%,#e2c99a,#b08e62 55%,#3a2d25)}
.profile-name{font-family:"Gelasio",Georgia,serif;font-size:25px;font-weight:400;color:var(--wine);margin-top:8px;letter-spacing:.5px}
.profile-bio{font-family:"Gelasio",Georgia,serif;font-size:9.6px;line-height:10.5px;color:#3a3a3a;margin-top:7px}

/* footer */
.site-footer{position:absolute;left:0;top:1173px;width:676px;height:27px;background:var(--wine)}
.copyright{position:absolute;left:107px;top:8px;font-family:"Gelasio",Georgia,serif;font-size:7.4px;color:#fff}
.social{position:absolute;left:513px;top:7px;display:flex;gap:4px}
.social span{width:12px;height:12px;border-radius:50%;background:#c46a73}
</style>
</head>
<body>
<div class="page">

  <header class="site-header">
    <div class="brand">
      <div class="brand-name">R. MORTON</div>
      <div class="brand-tagline">ORGANIZATIONAL CHANGE AND DEVELOPMENT</div>
    </div>
    <nav class="main-nav">
      <a class="active">HOME</a>
      <a>COMPANY</a>
      <a>AREAS OF EXPERTISE</a>
      <a>SERVICES</a>
      <a>CONTACT US</a>
    </nav>
  </header>

  <section class="hero">
    <div class="hero-photo" role="img" aria-label="Portrait of R. Morton in a black blazer, arms crossed"></div>
    <p class="hero-lead">Captured with your presentations - they were informative and to-the-point.</p>
    <h1 class="hero-title"><span class="big">WEBINAR</span><span class="sub">TRAINING INSTRUCTOR</span></h1>
    <div class="hero-button">LEARN MORE</div>
    <svg class="hero-arrow prev" viewBox="0 0 14 14"><circle cx="7" cy="7" r="6.3" fill="none" stroke="#e6b3b8" stroke-width="1"/><path d="M10 7H4M6.5 4.5L4 7l2.5 2.5" fill="none" stroke="#e6b3b8" stroke-width="1"/></svg>
    <svg class="hero-arrow next" viewBox="0 0 14 14"><circle cx="7" cy="7" r="6.3" fill="none" stroke="#e6b3b8" stroke-width="1"/><path d="M4 7h6M7.5 4.5L10 7 7.5 9.5" fill="none" stroke="#e6b3b8" stroke-width="1"/></svg>
  </section>

  <section class="roles">
    <div class="role" style="left:100px;width:80px">
      <svg viewBox="0 0 28 28"><circle cx="14" cy="14" r="12" fill="none" stroke="#fff" stroke-width="2.4"/><path d="M14 14l5-6" stroke="#fff" stroke-width="2.4" stroke-linecap="round"/><circle cx="14" cy="14" r="2.4" fill="#fff"/></svg>
      SENIOR FACILITATOR
    </div>
    <div class="role" style="left:184px;width:80px">
      <svg viewBox="0 0 28 28"><path d="M4 11h5l11-6v18L9 17H4z" fill="#fff"/><path d="M7 17l2 7h3l-1-7" fill="#fff"/><path d="M23 10l3-2M23 14h4M23 18l3 2" stroke="#fff" stroke-width="1.6"/></svg>
      KEYNOTE SPEAKER
    </div>
    <div class="role" style="left:263px;width:80px">
      <svg viewBox="0 0 28 28"><circle cx="14" cy="8" r="5.5" fill="#fff"/><path d="M4 27c0-8 4-12 10-12s10 4 10 12z" fill="#fff"/><path d="M14 15l-2 4 2 6 2-6z" fill="#333"/></svg>
      EXECUTIVE COACH
    </div>
    <div class="role active" style="left:347px;width:79px">
      <svg viewBox="0 0 28 28"><circle cx="14" cy="6" r="4.5" fill="#fff"/><path d="M7 27V16c0-3 3-5 7-5s7 2 7 5v11z" fill="#fff"/><rect x="2" y="13" width="12" height="3" fill="#fff"/></svg>
      WEBINAR TRAINING<br>INSTRUCTOR
    </div>
    <div class="role" style="left:431px;width:90px">
      <svg viewBox="0 0 28 28"><circle cx="14" cy="8" r="5.5" fill="#fff"/><path d="M5 27c0-8 4-12 9-12s9 4 9 12z" fill="#fff"/></svg>
      QUALITY MANAGEMENT<br>ADVISER
    </div>
    <div class="role" style="left:521px;width:56px">
      <svg viewBox="0 0 28 28"><circle cx="9" cy="9" r="4" fill="#fff"/><path d="M2 27c0-7 3-10 7-10s7 3 7 10z" fill="#fff"/><path d="M14 14l4-4 3 3 5-6" fill="none" stroke="#fff" stroke-width="1.8"/></svg>
      CLASSROOM<br>PRESENTER
    </div>
  </section>

  <!-- row 1 -->
  <article class="area" style="left:105px;top:367px;height:193px">
    <div class="area-photo short" role="img" aria-label="Group photo of a diverse team outdoors"><span class="plus">+</span></div>
    <h3 class="area-title">Diversity and cultural competence</h3>
    <p class="area-text">Lorem Ipsum is simply dummy text of the printing and typesetting industry. Lorem Ipsum has been the industry's standard dummy text ever since the 1500s, when an unknown printer took a galley of type and scrambled it to make a type specimen book.</p>
  </article>
  <article class="area" style="left:223px;top:367px;height:193px">
    <div class="area-photo tall" role="img" aria-label="Hands holding soil with a young sprout"><span class="plus">+</span></div>
    <h3 class="area-title">Organizational development</h3>
    <p class="area-text">Lorem Ipsum has been the industry's standard dummy text ever since the 1500s, when an unknown printer took a galley of type and scrambled it to make a type specimen book.</p>
  </article>
  <article class="area" style="left:340px;top:367px;height:193px">
    <div class="area-photo short" role="img" aria-label="Hand stopping falling dominoes"><span class="plus">+</span></div>
    <h3 class="area-title">Change management</h3>
    <p class="area-text">Lorem Ipsum is simply dummy text of the printing and typesetting industry. Lorem Ipsum has been the industry's standard dummy text ever since the 1500s, when an unknown printer took a galley of type and scrambled it to make a type specimen book.</p>
  </article>
  <article class="area" style="left:459px;top:367px;height:193px">
    <div class="area-photo tall" role="img" aria-label="Figure leading others up a staircase"><span class="plus">+</span></div>
    <h3 class="area-title">Leadership</h3>
    <p class="area-text">Lorem Ipsum has been the industry's standard dummy text ever since the 1500s, when an unknown printer took a galley of type and scrambled it to make a type specimen book.</p>
  </article>

  <!-- row 2 -->
  <article class="area" style="left:105px;top:576px;height:214px">
    <div class="area-photo tall" role="img" aria-label="Team working around a table in a meeting room"><span class="plus">+</span></div>
    <h3 class="area-title">Organizational dynamics</h3>
    <p class="area-text">Lorem Ipsum is simply dummy text of the printing and typesetting industry. Lorem Ipsum has been the industry's standard dummy text ever since the 1500s, when an unknown printer took a galley of type and scrambled it to make a type specimen book.</p>
  </article>
  <article class="area" style="left:223px;top:576px;height:214px">
    <div class="area-photo short" role="img" aria-label="Group of people jumping together on a beach"><span class="plus">+</span></div>
    <h3 class="area-title">Team-building</h3>
    <p class="area-text">Lorem Ipsum has been the industry's standard dummy text ever since the 1500s, when an unknown printer took a galley of type and scrambled it to make a type specimen book. Lorem Ipsum is simply dummy text of the printing and typesetting industry. Lorem Ipsum has been the industry's standard dummy text ever since the 1500s, when an unknown printer took a galley of type and scrambled it to make a type specimen book.</p>
  </article>
  <article class="area" style="left:340px;top:576px;height:214px">
    <div class="area-photo tall" role="img" aria-label="Rows of figures with one standing out"><span class="plus">+</span></div>
    <h3 class="area-title">Accountability</h3>
    <p class="area-text">Lorem Ipsum is simply dummy text of the printing and typesetting industry. Lorem Ipsum has been the industry's standard dummy text ever since the 1500s, when an unknown printer took a galley of type and scrambled it to make a type specimen book.</p>
  </article>
  <article class="area" style="left:459px;top:576px;height:214px">
    <div class="area-photo short" role="img" aria-label="Business people shaking hands across a table"><span class="plus">+</span></div>
    <h3 class="area-title">Negotiation</h3>
    <p class="area-text">Lorem Ipsum has been the industry's standard dummy text ever since the 1500s, when an unknown printer took a galley of type and scrambled it to make a type specimen book. Lorem Ipsum is simply dummy text of the printing and typesetting industry. Lorem Ipsum has been the industry's standard dummy text ever since the 1500s, when an unknown printer took a galley of type and scrambled it to make a type specimen book.</p>
  </article>

  <!-- row 3 -->
  <article class="area" style="left:105px;top:806px;height:192px">
    <div class="area-photo short" role="img" aria-label="Balanced stack of stones by the sea"><span class="plus">+</span></div>
    <h3 class="area-title">Work-life balance</h3>
    <p class="area-text">Lorem Ipsum is simply dummy text of the printing and typesetting industry. Lorem Ipsum has been the industry's standard dummy text ever since the 1500s, when an unknown printer took a galley of type and scrambled it to make a type specimen book. Lorem Ipsum is simply dummy text of the printing and typesetting industry.</p>
  </article>
  <article class="area" style="left:223px;top:806px;height:192px">
    <div class="area-photo tall" role="img" aria-label="Hand drawing a rising arrow chart"><span class="plus">+</span></div>
    <h3 class="area-title">Quality management</h3>
    <p class="area-text">Lorem Ipsum has been the industry's standard dummy text ever since the 1500s, when an unknown printer took a galley of type and scrambled it to make a type specimen book.</p>
  </article>
  <article class="area" style="left:340px;top:806px;height:192px">
    <div class="area-photo short" role="img" aria-label="Close-up of a disc"><span class="plus">+</span></div>
    <h3 class="area-title">DISC</h3>
    <p class="area-text">Lorem Ipsum is simply dummy text of the printing and typesetting industry. Lorem Ipsum has been the industry's standard dummy text ever since the 1500s, when an unknown printer took a galley of type and scrambled it to make a type specimen book. Lorem Ipsum is simply dummy text of the printing and typesetting industry.</p>
  </article>
  <article class="area" style="left:459px;top:806px;height:192px">
    <div class="area-photo tall" role="img" aria-label="Colleagues working together at a computer"><span class="plus">+</span></div>
    <h3 class="area-title">Web based trainings</h3>
    <p class="area-text">Lorem Ipsum has been the industry's standard dummy text ever since the 1500s, when an unknown printer took a galley of type and scrambled it to make a type specimen book.</p>
  </article>

  <section class="profile">
    <div class="avatar" role="img" aria-label="Round portrait of R. Morton"></div>
    <h2 class="profile-name">R. MORTON</h2>
    <p class="profile-bio">I have a PhD. in Counseling Psychology, MBA, B.S. in Human Development, Family Studies,<br>and a Master's Practitioner of Neurolinguistic Programming.</p>
  </section>

  <footer class="site-footer">
    <div class="copyright">© R.Morton 2014</div>
    <div class="social" aria-label="Social links"><span></span><span></span><span></span><span></span></div>
  </footer>

</div>
</body>
</html>
```